Stationery for consulting company
Strategic Thinking. Inclusive Solutions. Measurable Impact
Project: Stationery for consulting company
Business Cards and Stationery
Professional
Benedo Ofurame Phd
Senior Partner
Plot 9 Umoru Close Oregun, Ikeja Lagos - Nigeria
Benedo.ofura@velmarq.com
www.velmarq.com
fdsfdffdsd

```html
<!DOCTYPE html>
<html lang="en">
<head>
<meta charset="utf-8">
<title>Velmarq Consulting – Business Card</title>
<link href="https://fonts.googleapis.com/css2?family=Poppins:wght@400;500;600;700&display=swap" rel="stylesheet">
<style>
  :root{
    --bg:#e4e4e4;
    --green:#0d4f2d;
    --orange:#d9641e;
    --white:#ffffff;
    --ink:#2b2b2b;
    --muted:#8a8a8a;
  }
  *{margin:0;padding:0;box-sizing:border-box}
  html,body{width:1200px;height:901px;overflow:hidden;background:var(--bg);font-family:"Poppins",sans-serif}
  .canvas{position:relative;width:1200px;height:901px}
  .card{position:absolute;left:300px;width:600px;height:346px;border-radius:24px;overflow:hidden}
  .card-front{top:66px;background:var(--green)}
  .card-back{top:484px;background:var(--white)}

  .brand{position:absolute;display:flex;align-items:center}
  .brand-mark{border-radius:50%;flex:none}
  .brand-name{font-weight:600;text-transform:uppercase;line-height:1;white-space:nowrap}

  .card-front .brand{left:50%;top:50%;transform:translate(-50%,-50%);gap:20px}
  .card-front .brand-mark{width:90px;height:90px;background:var(--white)}
  .card-front .brand-name{color:var(--white);font-size:28px;letter-spacing:2.5px}

  .card-back .brand{right:36px;top:22px;gap:12px}
  .card-back .brand-mark{width:48px;height:48px;background:var(--orange)}
  .card-back .brand-name{color:var(--green);font-size:20px;letter-spacing:1.5px}

  .holder{position:absolute;left:34px;top:170px}
  .holder-name{font-size:23px;font-weight:700;color:var(--green);text-transform:uppercase;letter-spacing:.5px}
  .holder-name .degree{color:var(--orange)}
  .holder-role{font-size:12.5px;color:var(--muted);margin-top:2px}

  .contacts{position:absolute;left:34px;top:252px;list-style:none}
  .contacts li{display:flex;align-items:center;gap:8px;font-size:12px;color:var(--ink);line-height:20px}
  .contacts svg{width:11px;height:11px;fill:var(--ink)}

  .address{position:absolute;right:36px;top:252px;text-align:right;font-size:12px;line-height:20px;color:var(--ink)}

  .wave{position:absolute;left:0;bottom:0;width:600px;height:60px}
  .website{position:absolute;right:36px;bottom:12px;font-size:12px;color:var(--white)}
</style>
</head>
<body>
<main class="canvas">

  <section class="card card-front" aria-label="Business card front">
    <div class="brand">
      <span class="brand-mark"></span>
      <span class="brand-name">Velmarq Consulting</span>
    </div>
  </section>

  <section class="card card-back" aria-label="Business card back">
    <div class="brand">
      <span class="brand-mark"></span>
      <span class="brand-name">Velmarq Consulting</span>
    </div>

    <div class="holder">
      <p class="holder-name">Benedo Ofurame <span class="degree">PhD</span></p>
      <p class="holder-role">Senior Partner</p>
    </div>

    <ul class="contacts">
      <li>
        <svg viewBox="0 0 24 24" aria-hidden="true"><path d="M6.6 10.8a15.1 15.1 0 0 0 6.6 6.6l2.2-2.2a1 1 0 0 1 1-.25 11.4 11.4 0 0 0 3.6.57 1 1 0 0 1 1 1V20a1 1 0 0 1-1 1A17 17 0 0 1 3 4a1 1 0 0 1 1-1h3.5a1 1 0 0 1 1 1c0 1.25.2 2.45.57 3.6a1 1 0 0 1-.25 1z"/></svg>
        +234 (0) 801 555 0147
      </li>
      <li>
        <svg viewBox="0 0 24 24" aria-hidden="true"><path d="M2 5h20v14H2z M2 5l10 8 10-8" /></svg>
        Benedo.ofura@velmarq.com
      </li>
    </ul>

    <p class="address">Plot 9 Umoru Close Oregun<br>Ikeja Lagos - Nigeria</p>

    <svg class="wave" viewBox="0 0 600 60" preserveAspectRatio="none" aria-hidden="true">
      <path d="M0 28 C140 20 300 22 450 36 C300 28 140 28 0 36 Z" fill="var(--orange)"/>
      <path d="M0 44 C180 36 380 42 600 20 L600 60 L0 60 Z" fill="var(--green)"/>
    </svg>
    <p class="website">www.velmarq.com</p>
  </section>

</main>
</body>
</html>
```